Looking for an amazing business card for a thriving DJ business

We need a business card design for a DJ company based in South Florida. The DJ company specializes in weddings, parties, bar mitzvahs, corporate events, proms, and reunions. We are looking for a modern, simple business card design. The card should state DJ Marlow K.
Updates

The name on the card should be DJ Marlow K

Industry/Entity Type

Entertainment Industry

Contact Information for Business Card

DJ Marlow K
512.447.2086
atxdjmarlowk@quellmail.com
https://www.facebook.com/DjMarlowK/
https://www.instagram.com/djmarlow.k/
www.djmarlowk.net

Font styles to use
Serif
Sans Serif

Requirements
Must have
• My business card has to be awesome.
Should not have
• The card has to have personality.

```html
<!DOCTYPE html>
<html lang="en">
<head>
<meta charset="utf-8">
<title>DJ Marlow K — Business Card</title>
<link rel="stylesheet" href="https://fonts.googleapis.com/css2?family=Lato:wght@400;700&display=swap">
<style>
  :root {
    --stage: #d8d1c6;
    --card-cream: #f1e9dc;
    --card-dark: #2f2b29;
    --gold: #c18b3c;
    --gold-soft: #d3a55e;
    --ink-light: #ece2d2;
  }
  html, body {
    margin: 0;
    padding: 0;
    width: 1200px;
    height: 1047px;
    overflow: hidden;
    background: var(--stage);
  }
  .business-card {
    position: absolute;
    left: 80px;
    top: 242px;
    width: 1040px;
    height: 563px;
    filter: drop-shadow(0 10px 24px rgba(0,0,0,0.18));
  }
  .business-card svg { display: block; width: 100%; height: 100%; }
  .card-name {
    font-family: 'Lato', sans-serif;
    font-weight: 700;
    font-size: 32px;
    fill: var(--gold);
  }
  .contact-line {
    font-family: 'Lato', sans-serif;
    font-weight: 400;
    font-size: 19px;
    fill: var(--ink-light);
  }
  .brand-name {
    font-family: 'Lato', sans-serif;
    font-weight: 700;
    font-size: 30px;
    fill: var(--gold);
  }
  .icon { fill: none; stroke: var(--gold-soft); stroke-width: 1.6; }
  .icon-fill { fill: var(--gold-soft); }
</style>
</head>
<body>
<div class="business-card">
  <svg viewBox="0 0 878 475" xmlns="http://www.w3.org/2000/svg">
    <defs>
      <clipPath id="card-shape"><rect width="878" height="475" rx="14"/></clipPath>
    </defs>
    <g clip-path="url(#card-shape)">
      <rect class="card-face" width="878" height="475" fill="var(--card-cream)"/>
      <path class="dark-wave" fill="var(--card-dark)"
        d="M0,288 C120,240 250,228 360,285 C440,330 520,392 620,392 C730,392 810,335 878,282 L878,475 L0,475 Z"/>
      <path class="gold-swoosh" fill="var(--gold)"
        d="M0,285 C110,226 265,210 468,318 C275,236 125,240 0,277 Z"/>
    </g>

    <text class="card-name" x="57" y="80">DJ Marlow K</text>
    <rect class="name-rule" x="58" y="96" width="65" height="2.5" fill="var(--gold)"/>

    <g class="brand-mark">
      <circle cx="657" cy="197" r="112" fill="none" stroke="var(--gold)" stroke-width="2"/>
      <text class="brand-name" x="657" y="207" text-anchor="middle">Brightnote</text>
    </g>

    <g class="contact-list">
      <path class="icon-fill" d="M53,317 h16 a2,2 0 0 1 2,2 v3 h-4 v-2 h-12 v2 h-4 v-3 a2,2 0 0 1 2,-2 z M55,323 h12 l3,7 h-18 z"/>
      <text class="contact-line" x="90" y="330">512.447.2086</text>

      <rect class="icon" x="52" y="346" width="18" height="12"/>
      <path class="icon" d="M52,346 l9,7 l9,-7"/>
      <text class="contact-line" x="90" y="359">atxdjmarlowk@quellmail.com</text>

      <circle class="icon" cx="61" cy="379" r="7"/>
      <text class="contact-line" x="90" y="386">www.crowdlink.net/DjMarlowK/</text>

      <circle class="icon" cx="61" cy="405" r="7"/>
      <text class="contact-line" x="90" y="412">www.photolane.net/djmarlow.k/</text>

      <circle class="icon" cx="61" cy="434" r="7"/>
      <ellipse class="icon" cx="61" cy="434" rx="3" ry="7"/>
      <path class="icon" d="M54,434 h14"/>
      <text class="contact-line" x="90" y="441">www.djmarlowk.net</text>
    </g>
  </svg>
</div>
</body>
</html>
```